Mental Health and Marriage & Family Counseling Office Business Card Design

I work with a wide range of emotional and behavioral issues providing services that span from therapy for depression and grief counseling to parenting support, couples counseling and beyond. In a comfortable and supportive atmosphere, I offer a highly personalized approach tailored to each of my clients individual needs to help attain the personal growth they’re striving for. Providing individual, couples and family counseling.
Treatment specialization includes: Therapy for Depression and Anxiety, Couples Counseling, Family Counseling, Parenting Support, Grief Counseling, Work and Career issues, Stress Management, Conflict Resolution. I would like to see designs that use the colors "of a Peacock feather" , such as blues and greens, etc.

Industry/Entity Type

Business

Contact Information for Business Card

Delia K. Fenwick, MS, LPC
Licensed Professional Counselor
415 Harrowgate Lane Suite 231
Jacksonville, NC 28593

(910) 487-6124 Fax: (910) 487-6125
www.deliafenwicklpc.example
delia@deliafenwicklpc.example

```html
<!DOCTYPE html>
<html lang="en">
<head>
<meta charset="utf-8">
<title>Delia K. Fenwick, MS, LPC – Business Card</title>
<link rel="stylesheet" href="https://fonts.googleapis.com/css2?family=Questrial&display=swap">
<style>
  :root {
    --bg: #e9ecef;
    --card: #ffffff;
    --cyan: #1fb1e6;
    --teal-dark: #1b6f86;
    --green: #1e8a45;
    --ornament: #1cb5ec;
    --ornament-faint: #d6ecf8;
  }
  * { margin: 0; padding: 0; box-sizing: border-box; }
  html, body {
    width: 1200px; height: 800px; overflow: hidden;
    background: var(--bg);
    font-family: "Questrial", "Century Gothic", sans-serif;
  }
  .stage {
    width: 1200px; height: 800px;
    display: flex; align-items: center; justify-content: center; gap: 40px;
  }
  .card {
    position: relative;
    width: 560px; height: 320px;
    background: var(--card);
    box-shadow: 0 6px 18px rgba(0,0,0,0.18);
    overflow: hidden;
  }

  /* Front */
  .audience {
    position: absolute;
    width: 76px; height: 76px; border-radius: 50%;
    background: var(--green); color: #fff;
    display: flex; align-items: center; justify-content: center;
    font-size: 12px;
  }
  .audience--individuals { left: 92px; top: 14px; }
  .audience--couples { left: 206px; top: 36px; }
  .audience--families { left: 320px; top: 58px; }

  .name {
    position: absolute; left: 26px; top: 136px;
    font-size: 31px; line-height: 36px; color: var(--cyan); letter-spacing: 0.5px;
    font-weight: 400; white-space: nowrap;
  }
  .name-rule {
    position: absolute; left: 20px; top: 176px;
    width: 430px; height: 2px; background: var(--cyan);
  }
  .title {
    position: absolute; left: 58px; top: 182px;
    font-size: 19px; line-height: 22px; color: var(--teal-dark);
  }
  .contact-lines {
    position: absolute; left: 78px; top: 210px;
    display: grid; grid-template-columns: 70px 16px auto;
    font-size: 17px; line-height: 19px;
  }
  .contact-lines dt { color: var(--teal-dark); }
  .contact-lines .sep { color: var(--teal-dark); }
  .contact-lines dd { color: var(--cyan); }
  .address {
    position: absolute; left: 24px; top: 254px;
    font-style: normal; font-size: 17px; line-height: 19px;
    color: var(--teal-dark);
  }
  .web {
    position: absolute; right: 14px; bottom: 10px;
    text-align: right; font-size: 16px; line-height: 19px;
    color: var(--teal-dark);
  }
  .ornament-front {
    position: absolute; right: 22px; top: 182px;
    width: 100px; height: 92px; border-radius: 16px;
    background: var(--ornament);
  }

  /* Back */
  .specialties {
    position: absolute; left: 34px; top: 30px;
    list-style: none;
  }
  .specialties li {
    display: flex; align-items: center; gap: 9px;
    font-size: 13px; line-height: 24px;
    color: var(--cyan); text-transform: uppercase; letter-spacing: 0.3px;
  }
  .specialties li::before {
    content: ""; width: 11px; height: 11px; border-radius: 50%;
    background: var(--green); flex: none;
  }
  .ornament-back {
    position: absolute; right: 30px; bottom: 14px;
    width: 250px; height: 200px; border-radius: 30px;
    background: var(--ornament-faint);
  }
</style>
</head>
<body>
<main class="stage">
  <section class="card card--front" aria-label="Business card front">
    <div class="audience audience--individuals">Individuals</div>
    <div class="audience audience--couples">Couples</div>
    <div class="audience audience--families">Families</div>

    <h1 class="name">Delia K. Fenwick, MS, LPC</h1>
    <div class="name-rule"></div>
    <p class="title">Licensed Professional Counselor</p>

    <dl class="contact-lines">
      <dt>Phone</dt><span class="sep">:</span><dd>(910) 487-6124</dd>
      <dt>Fax</dt><span class="sep">:</span><dd>(910) 487-6125</dd>
    </dl>

    <address class="address">415 Harrowgate Lane Suite 231<br>Jacksonville, NC 28593</address>

    <div class="ornament-front" role="img" aria-label="Decorative vine ornament with heart-shaped leaves"></div>

    <p class="web">www.deliafenwicklpc.example<br>delia@deliafenwicklpc.example</p>
  </section>

  <section class="card card--back" aria-label="Business card back">
    <ul class="specialties">
      <li>Therapy for Depression and Anxiety</li>
      <li>Couples Counseling</li>
      <li>Family Counseling</li>
      <li>Parenting Support</li>
      <li>Grief Counseling</li>
      <li>Work and Career Issues</li>
      <li>Stress Management</li>
      <li>Conflict Resolution</li>
    </ul>
    <div class="ornament-back" role="img" aria-label="Faint decorative vine ornament with heart-shaped leaves"></div>
  </section>
</main>
</body>
</html>
```